HTML Web layout / data visualization for an information software application

We have a product used by patent analysts to allow them examine information stored in patents - particularly those patents that include biological sequences like DNA, RNA, and protein.

When the user opens up a particular patent, they currently see a very poorly organized wall of text, presenting fields of data to them in unorganized ways. We have attached screenshots of the current interface.

The project is to redesign that layout so that the same information is presented in a way which is brings important data to the the eyes of the user, categorizes data appropriately, and is visually appealing. We have proposed logical categorizations of data in the document called "Fields documentation."

The deliverable should be an HTML5 file that renders one or more of the examples of records we've provided in your new design.

Description of files:

"Examples of records badly displayed": MS Word file that shows three different examples of the records we would like to better visualize.

"screengrab1.tiff" and "screengrab2.tiff": pictures of how these records sit inside of our product. This is presented to give you a sense of screen real estate, our look and feel, and colors. We do not want the whole screen redesigned - just the record display itself.

"Fields documentation": detailed documentation of what each field means. We have tried to group them logically for you, and have also attempted to inform you as to which fields are linked to others.

Hi all,

Thanks for the designs so far. Unfortunately, nearly every design fails to understand the nature of the project. The problem we have is not about fonts and colors (although those matter). It is about grouping information together and displaying data in a way that provides insight. In the original brief, we say:

The document we have uploaded called "Fields documentation" is the most important document. We sense that very few of you have taken it into account. It provides notes on the nature of the data in the report and gives signs of the ways in which a creative designer might help to arrange the content.

Thanks for your consideration of this project.

TM

Target Market(s)

Patent analysts, heavily educated scientists, Ph.Ds.

Industry/Entity Type

Software

```html
<!DOCTYPE html>
<html lang="en">
<head>
<meta charset="utf-8">
<title>Patent Sequence Record – Claims</title>
<link rel="stylesheet" href="https://fonts.googleapis.com/css2?family=Open+Sans:wght@400;600&display=swap">
<style>
  :root{
    --teal-deep:#2a9fa5;
    --teal-mid:#79c8cb;
    --glow:#f4fafa;
    --sidebar-bg:#ececec;
    --sidebar-line:#ffffff;
    --sidebar-text:#8e9599;
    --panel-bg:#ffffff;
    --field-bg:#eaf6fb;
    --field-border:#cfe6ef;
    --field-text:#0d4f6c;
    --heading:#0b4f6f;
    --body-text:#5a5f63;
    --accent-top:#38c6ff;
    --accent-bottom:#0a9ff0;
    --icon:#19a9ec;
  }
  *{box-sizing:border-box;margin:0;padding:0}
  html,body{width:1200px;height:917px;overflow:hidden}
  body{
    font-family:"Open Sans",Arial,sans-serif;
    background:
      radial-gradient(ellipse 620px 520px at 600px 80px,var(--glow) 0%,rgba(244,250,250,.6) 35%,rgba(244,250,250,0) 75%),
      radial-gradient(ellipse 900px 800px at 600px 200px,var(--teal-mid) 0%,var(--teal-deep) 100%);
    position:relative;
  }
  .record-sidebar{
    position:absolute;left:154px;top:173px;width:214px;height:634px;
    background:var(--sidebar-bg);border-radius:3px 0 0 3px;
    box-shadow:0 1px 4px rgba(0,0,0,.08);
    list-style:none;padding-top:2px;
  }
  .record-sidebar li{
    height:38px;padding-left:8px;display:flex;align-items:center;
    font-size:13.3px;color:var(--sidebar-text);
    border-bottom:1px solid var(--sidebar-line);
  }
  .record-sidebar li:first-child{height:40px}
  .record-sidebar li.is-active{
    margin:0 0 0 3px;padding-left:5px;height:36px;
    background:linear-gradient(var(--accent-top),var(--accent-bottom));
    color:#fff;justify-content:space-between;padding-right:18px;border:none;
  }
  .record-panel{
    position:absolute;left:369px;top:167px;width:677px;height:661px;
    background:var(--panel-bg);border-radius:3px;
    box-shadow:0 1px 6px rgba(0,0,0,.1);
  }
  .field-value{
    position:absolute;left:7px;width:661px;height:31px;
    background:var(--field-bg);padding-left:17px;
    display:flex;align-items:center;
    font-size:13.3px;color:var(--field-text);
  }
  .claims-heading{
    position:absolute;left:11px;top:248px;
    font-size:14.7px;font-weight:600;color:var(--heading);
  }
  .claim-header{
    position:absolute;left:8px;width:662px;height:31px;
    background:var(--field-bg);border:1px solid var(--field-border);
    display:flex;align-items:center;justify-content:space-between;
    padding:0 5px 0 9px;font-size:14.7px;color:var(--heading);
  }
  .claim-body{
    position:absolute;left:13px;top:314px;width:652px;
    font-size:12px;line-height:20.2px;color:var(--body-text);
  }
</style>
</head>
<body>
  <ul class="record-sidebar">
    <li>Identifier</li>
    <li>Patent sequence location</li>
    <li>Organism (non-normalized name)</li>
    <li>Organism</li>
    <li>Taxonomy ID</li>
    <li>Patent SEQ ID NO</li>
    <li class="is-active">Claims
      <svg width="14" height="14" viewBox="0 0 14 14" aria-hidden="true"><path d="M3 1.5 L9.5 7 L3 12.5" fill="none" stroke="#fff" stroke-width="3"/></svg>
    </li>
  </ul>

  <section class="record-panel">
    <div class="field-value" style="top:12px">US6812339-13070</div>
    <div class="field-value" style="top:53px">probable disclosure (not found by automated parsing)</div>
    <div class="field-value" style="top:94px">Human</div>
    <div class="field-value" style="top:130px">Homo sapiens (human)</div>
    <div class="field-value" style="top:168px">9606</div>
    <div class="field-value" style="top:205px">13070</div>

    <h2 class="claims-heading">Claims Details</h2>

    <div class="claim-header" style="top:278px">Claims Title Here
      <svg width="19" height="19" viewBox="0 0 20 20" aria-hidden="true"><circle cx="10" cy="10" r="10" fill="var(--icon)"/><path d="M5.5 8 L10 12.5 L14.5 8" fill="none" stroke="#fff" stroke-width="2.2"/></svg>
    </div>
    <p class="claim-body">
      (a) a detection reagent consisting of a segment of SEQ ID NO:12025,&nbsp; wherein the segment comprises at least 15 con-<br>
      tiguous nucleotides of SEQ ID NO:23778, and wherein the at least 15 contiguous nucleotides<br>
      include nucleotide 301 of SEQ ID NO:23778, and further wherein&nbsp; nucleotide 301 of SEQ ID NO:23778 is ‘G’,<br>
      (b) a detection reagent consisting of segment of SEQ ID NO:12025, wherein the segment comprises at least 15 con-<br>
      tiguous nucleotides of SEQ ID NO:23778, and wherein the at least 15 contiguous nucleotides<br>
      include nucleotide 301 of SEQ ID NO:23778, and further wherein nucleotide 301 of SEQ ID NO:23778 is ‘A’, and&nbsp; (c) a<br>
      detection reagent which is entirely complementary to the detection reagent of (a) or (b).
    </p>

    <div class="claim-header" style="top:466px">Claims Title Here
      <svg width="19" height="19" viewBox="0 0 20 20" aria-hidden="true"><circle cx="10" cy="10" r="10" fill="var(--icon)"/><path d="M5.5 8 L10 12.5 L14.5 8" fill="none" stroke="#fff" stroke-width="2.2"/></svg>
    </div>
    <div class="claim-header" style="top:502px">Claims Title Here
      <svg width="19" height="19" viewBox="0 0 20 20" aria-hidden="true"><circle cx="10" cy="10" r="10" fill="var(--icon)"/><path d="M5.5 8 L10 12.5 L14.5 8" fill="none" stroke="#fff" stroke-width="2.2"/></svg>
    </div>
    <div class="claim-header" style="top:537px">Claims Title Here
      <svg width="19" height="19" viewBox="0 0 20 20" aria-hidden="true"><circle cx="10" cy="10" r="10" fill="var(--icon)"/><path d="M5.5 8 L10 12.5 L14.5 8" fill="none" stroke="#fff" stroke-width="2.2"/></svg>
    </div>
    <div class="claim-header" style="top:572px">Claims Title Here
      <svg width="19" height="19" viewBox="0 0 20 20" aria-hidden="true"><circle cx="10" cy="10" r="10" fill="var(--icon)"/><path d="M5.5 8 L10 12.5 L14.5 8" fill="none" stroke="#fff" stroke-width="2.2"/></svg>
    </div>
    <div class="claim-header" style="top:608px">Claims Title Here
      <svg width="19" height="19" viewBox="0 0 20 20" aria-hidden="true"><circle cx="10" cy="10" r="10" fill="var(--icon)"/><path d="M5.5 8 L10 12.5 L14.5 8" fill="none" stroke="#fff" stroke-width="2.2"/></svg>
    </div>
  </section>
</body>
</html>
```